Business Card Design for Real Estate Company

I am looking for a business card design that will catch my client's attention.

Industry/Entity Type

Business

Requirements
Must have
• Please have the following information in the business card design. You can substitute the "Office, Mobile, email, and web" with an icon or some other design you may think will go well with the business card.

Derek Osmund
482 W. Fenwick St., Suite 310
Pasadena, CA 91348
Office: 626.748.1196
Mobile: 626.913.4071
email: Derek@CrestviewPropertyWalk.example
web: www.CrestviewPropertyWalk.example

```html
<!DOCTYPE html>
<html lang="en">
<head>
<meta charset="utf-8">
<title>Crestview Property Walk – Business Card</title>
<link href="https://fonts.googleapis.com/css2?family=Arimo:wght@400;700&family=Handlee&display=swap" rel="stylesheet">
<style>
  :root {
    --brown: #45290f;
    --brown-text: #4a3312;
    --cream: #eadfcd;
    --white: #ffffff;
    --ink: #111111;
    --accent: #e0621f;
  }
  * { margin: 0; padding: 0; box-sizing: border-box; }
  html, body { width: 1052px; height: 1200px; overflow: hidden; background: var(--white); }
  body { font-family: "Arimo", Arial, sans-serif; }
  .card { position: relative; width: 1052px; height: 1200px; background: var(--white); }

  .brand-panel {
    position: absolute; left: 0; top: 0; width: 1052px; height: 603px;
    border: 2px solid var(--ink); background: var(--white);
    display: flex; align-items: center; justify-content: center; gap: 26px;
  }
  .brand-dot { width: 70px; height: 70px; border-radius: 50%; background: var(--accent); flex: none; }
  .brand-name {
    font-family: "Arimo", Arial, sans-serif; font-weight: 700;
    font-size: 64px; color: var(--brown-text); letter-spacing: 1px;
  }

  .info-panel {
    position: absolute; left: 0; top: 603px; width: 1052px; height: 527px;
    background: var(--brown);
  }
  .tagline {
    position: absolute; right: 28px; top: 26px;
    font-family: "Handlee", cursive; font-size: 33px; color: var(--cream);
  }
  .benefit {
    position: absolute; right: 0; height: 33px;
    background: var(--white); color: var(--ink);
    font-weight: 700; font-size: 24.5px; line-height: 33px;
    padding: 0 28px 0 5px; white-space: nowrap;
  }
  .agent { position: absolute; left: 190px; top: 427px; color: var(--white); }
  .agent-name { font-size: 45px; font-weight: 700; line-height: 1; }
  .agent-phone { font-size: 25px; font-weight: 700; margin-top: 10px; margin-left: 18px; }

  .office-contact {
    position: absolute; left: 0; top: 1130px; width: 1052px; height: 70px;
    display: flex; flex-direction: column; align-items: center; justify-content: center;
    color: var(--brown-text); font-weight: 700;
  }
  .office-address { font-size: 24px; line-height: 29px; }
  .office-lines { font-size: 16px; line-height: 21px; }
</style>
</head>
<body>
<div class="card">
  <header class="brand-panel">
    <span class="brand-dot"></span>
    <span class="brand-name">Crestview Property Walk</span>
  </header>

  <section class="info-panel">
    <p class="tagline">Your Local Real Estate Connection</p>
    <p class="benefit" style="top:90px;">Ability to target home searches</p>
    <p class="benefit" style="top:152px;">Expertise about neighborhood features</p>
    <p class="benefit" style="top:214px;">Support through the closing and beyond</p>
    <p class="benefit" style="top:276px;">Get a positive, helpful partner for buying or selling a home</p>
    <p class="benefit" style="top:339px;">Trusted resource for answers about the process</p>
    <p class="benefit" style="top:401px;">Innovative marketing strategies</p>
    <p class="benefit" style="top:463px;">Strong negotiation skills</p>

    <div class="agent">
      <p class="agent-name">Derek Osmund</p>
      <p class="agent-phone">(626) 913-4071</p>
    </div>
  </section>

  <footer class="office-contact">
    <p class="office-address">Crestview Property Walk , 482 W. Fenwick St., Suite 310. Pasadena, CA, 91348</p>
    <p class="office-lines">Office: 626.748.1196 · Derek@CrestviewPropertyWalk.example · www.CrestviewPropertyWalk.example</p>
  </footer>
</div>
</body>
</html>
```